Technology Solutions Provider

Let’s design a business card that will be as simple and bold at the same time. Name, email address, website & phone number.

Target Market(s)

Small to Medium Size Business

Industry/Entity Type

It Professional

Contact Information for Business Card

Name, email, website, phone numbers

Font styles to use
Sans Serif

Colors
ec1f27
f04a50
dddddd
919191
000000
ffffff

Requirements
Must have
• Clean simple look using my existing logo. I just need to the basic contact information on this card.
Nice to have
• Im considering the square size card versus the standard size business card.
Should not have
• No Mailing Address, no list of services.

```html
<!DOCTYPE html>
<html lang="en">
<head>
<meta charset="utf-8">
<title>helixware business cards</title>
<link rel="stylesheet" href="https://fonts.googleapis.com/css2?family=Jura:wght@500;600&family=Tinos&display=swap">
<style>
  :root {
    --brand-red: #ec1f27;
    --ink: #050707;
    --paper: #ffffff;
    --rule: #333333;
    --tagline: #555555;
    --stage-band: #000000;
  }
  html, body {
    margin: 0;
    padding: 0;
    width: 1200px;
    height: 1000px;
    overflow: hidden;
    background: var(--paper);
  }
  .canvas {
    position: relative;
    width: 1200px;
    height: 1000px;
    font-family: "Jura", sans-serif;
  }
  .floor-band {
    position: absolute;
    left: 0; top: 774px;
    width: 1200px; height: 226px;
    background: var(--stage-band);
  }
  .card { position: absolute; box-sizing: border-box; overflow: hidden; }

  /* standard card, back */
  .standard-back {
    left: 35px; top: 51px; width: 523px; height: 298px;
    background: var(--ink);
    display: flex; align-items: center; justify-content: center;
  }
  .back-name {
    color: var(--brand-red);
    font-weight: 600;
    font-size: 44px;
    letter-spacing: 1px;
  }

  /* standard card, front */
  .standard-front {
    left: 599px; top: 51px; width: 523px; height: 299px;
    background: var(--paper);
    border: 1px solid var(--rule);
  }
  .standard-front .side-block {
    position: absolute; left: 0; top: 0;
    width: 209px; height: 100%;
    background: var(--ink);
  }
  .standard-front .wordmark {
    position: absolute; left: 218px; top: 28px;
    font-size: 46px; font-weight: 600; color: var(--ink);
    letter-spacing: 1px; line-height: 1;
  }
  .tagline {
    font-family: "Tinos", serif;
    color: var(--tagline);
    white-space: nowrap;
  }
  .standard-front .tagline {
    position: absolute; left: 220px; top: 67px;
    font-size: 19px; word-spacing: 3px;
  }
  .standard-front .contact {
    position: absolute; left: 217px; top: 234px;
    font-size: 15px; line-height: 19.5px; color: var(--ink);
    font-weight: 500;
  }

  /* square card, back */
  .square-back {
    left: 322px; top: 477px; width: 236px; height: 236px;
    background: var(--ink);
    display: flex; align-items: center; justify-content: center;
  }
  .square-back .back-name { font-size: 30px; }

  /* square card, front */
  .square-front {
    left: 599px; top: 477px; width: 236px; height: 235px;
    background: var(--paper);
    border: 2px solid var(--ink);
  }
  .square-front .lockup {
    position: absolute; left: 0; top: 0; width: 100%; height: 68px;
    display: flex; align-items: center; justify-content: center; gap: 6px;
  }
  .square-front .lockup-divider {
    width: 1px; height: 36px; background: var(--ink);
  }
  .square-front .lockup-text { display: flex; flex-direction: column; }
  .square-front .wordmark {
    font-size: 21px; font-weight: 600; color: var(--ink); line-height: 1;
  }
  .square-front .tagline { font-size: 9.5px; margin-top: 2px; }
  .square-front .middle-band {
    position: absolute; left: 0; top: 68px; width: 100%; height: 98px;
    background: var(--ink);
  }
  .square-front .contact {
    position: absolute; left: 0; top: 184px; width: 100%;
    text-align: center; font-size: 11px; line-height: 14.5px;
    color: var(--ink); font-weight: 500;
  }
</style>
</head>
<body>
<main class="canvas">
  <section class="card standard-back">
    <span class="back-name">helixware</span>
  </section>

  <section class="card standard-front">
    <div class="side-block"></div>
    <div class="wordmark">helixware</div>
    <div class="tagline">technology solutions provider</div>
    <div class="contact">
      hello@helixware.com<br>
      www.helixware.com<br>
      +60 - 1298765430
    </div>
  </section>

  <section class="card square-back">
    <span class="back-name">helixware</span>
  </section>

  <section class="card square-front">
    <div class="lockup">
      <div class="lockup-divider"></div>
      <div class="lockup-text">
        <span class="wordmark">helixware</span>
        <span class="tagline">technology solutions provider</span>
      </div>
    </div>
    <div class="middle-band"></div>
    <div class="contact">
      hello@helixware.com<br>
      www.helixware.com<br>
      +60 - 1298765430
    </div>
  </section>

  <div class="floor-band"></div>
</main>
</body>
</html>
```